LOCAL TAXI SERVICE NEEDS A BANNER AD DESIGN

NEED BANNER AD DESIGN FOR TAXI SERVICE IN NJ. WE PROVIDE LOCAL AND LONG DISTANCE TRANSPORTATION. OUR MAIN BASE OF CUSTOMER GO TO THE MAJOR AIRPORTS IN THE TRI STATE AREA. I WANT TO OFFER A SPECIAL GOING TO HOLMBRIDGE AIRPORT OF $35.00 WITH A COUPON CODE OF PW 12. THIS BANNER AD WILL BE USED FOR MY PALWIRE PAGE

Target Market(s)

PEOPLE WHO TRAVEL A LOT

Industry/Entity Type

Taxi

Font styles to use
Serif
Sans Serif

Colors
0792cd
0255a3
33a6d7
85cae6
cee9f5
ecf7fb
ffffff

Requirements
Must have
• MY COMPANY NAME: DORVAN'S TAXI

```html
<!DOCTYPE html>
<html lang="en">
<head>
<meta charset="utf-8">
<title>Dorvan's Taxi – Holmbridge Airport Banner</title>
<link rel="stylesheet" href="https://fonts.googleapis.com/css2?family=Oswald:wght@500;600&display=swap">
<style>
  :root {
    --sky-blue: #33a6d7;
    --soft-blue: #85cae6;
    --deep-blue: #0792cd;
    --pale-blue: #cee9f5;
    --ink: #222222;
    --white: #ffffff;
    --page: #eeeeee;
    --sky-grey: #c9ccce;
    --cloud-dark: #6d7276;
    --field: #8a7a66;
    --road: #4a4c4f;
  }
  * { margin: 0; padding: 0; box-sizing: border-box; }
  html, body {
    width: 867px;
    height: 1200px;
    overflow: hidden;
    background: var(--page);
    font-family: "Oswald", "Arial Narrow", sans-serif;
  }
  .banner {
    position: absolute;
    left: 33px;
    width: 800px;
    height: 419px;
    overflow: hidden;
    background: var(--sky-blue);
    box-shadow: 0 4px 14px rgba(0,0,0,0.25);
  }
  .banner--flat { top: 43px; }
  .banner--faceted {
    top: 576px;
    background: linear-gradient(135deg, var(--pale-blue) 0%, var(--soft-blue) 35%, var(--sky-blue) 100%);
  }
  .scene-photo {
    position: absolute;
    inset: 0;
    clip-path: polygon(0 0, 57.5% 0, 31.6% 100%, 0 100%);
    background: linear-gradient(180deg, var(--sky-grey) 0%, var(--cloud-dark) 38%, var(--sky-grey) 55%, var(--field) 60%, var(--road) 72%, var(--road) 100%);
  }
  .car-photo {
    position: absolute;
    left: 111px;
    top: 160px;
    width: 396px;
    height: 230px;
    border-radius: 60px 90px 30px 30px;
    background: linear-gradient(180deg, #f4f5f6 0%, #dcdee0 60%, #9da1a5 100%);
  }
  .brand {
    position: absolute;
    left: 8px;
    top: 17px;
    height: 40px;
    display: flex;
    align-items: center;
    gap: 8px;
    padding: 0 14px 0 6px;
    background: var(--ink);
  }
  .brand__mark {
    width: 28px;
    height: 28px;
    background: var(--sky-blue);
  }
  .brand__name {
    color: var(--white);
    font-weight: 500;
    font-size: 22px;
    letter-spacing: 0.5px;
  }
  .offer {
    position: absolute;
    right: 15px;
    color: var(--white);
    text-align: right;
    font-weight: 600;
    line-height: 1.1;
  }
  .offer__lead { top: 20px; font-size: 30px; }
  .offer__destination { top: 56px; font-size: 37px; }
  .offer__label { top: 170px; font-size: 30px; }
  .price-box {
    position: absolute;
    right: 0;
    top: 215px;
    width: 153px;
    height: 66px;
    background: var(--ink);
    color: var(--white);
    font-weight: 600;
    font-size: 40px;
    text-align: right;
    padding-right: 15px;
    line-height: 66px;
  }
  .coupon-box {
    position: absolute;
    right: 0;
    top: 291px;
    width: 263px;
    height: 104px;
    background: var(--ink);
    color: var(--white);
    text-align: right;
    padding: 10px 15px 0 0;
    font-weight: 600;
  }
  .coupon-box__label { display: block; font-size: 23px; line-height: 1.2; }
  .coupon-box__code { display: block; font-size: 50px; line-height: 1.1; }
</style>
</head>
<body>
  <section class="banner banner--flat">
    <div class="scene-photo" role="img" aria-label="Photo of an open highway under grey storm clouds"></div>
    <div class="car-photo" role="img" aria-label="Photo of a white sedan taxi"></div>
    <div class="brand"><span class="brand__mark"></span><span class="brand__name">DORVAN'S TAXI</span></div>
    <p class="offer offer__lead">WANT TO GOING</p>
    <p class="offer offer__destination">HOLMBRIDGE AIRPORT ?</p>
    <p class="offer offer__label">SPECIAL OFFER PRICE</p>
    <div class="price-box">$35.00</div>
    <div class="coupon-box"><span class="coupon-box__label">USE THIS COUPON CODE</span><span class="coupon-box__code">PW12</span></div>
  </section>

  <section class="banner banner--faceted">
    <div class="scene-photo" role="img" aria-label="Photo of an open highway under grey storm clouds"></div>
    <div class="car-photo" role="img" aria-label="Photo of a white sedan taxi"></div>
    <div class="brand"><span class="brand__mark"></span><span class="brand__name">DORVAN'S TAXI</span></div>
    <p class="offer offer__lead">WANT TO GOING</p>
    <p class="offer offer__destination">HOLMBRIDGE AIRPORT ?</p>
    <p class="offer offer__label">SPECIAL OFFER PRICE</p>
    <div class="price-box">$35.00</div>
    <div class="coupon-box"><span class="coupon-box__label">USE THIS COUPON CODE</span><span class="coupon-box__code">PW12</span></div>
  </section>
</body>
</html>
```